Baby Muslin Wrap/Swaddle Box Packaging Design

We are a company that sells baby muslin wraps. We currently sell cotton and bamboo baby muslin wraps in egdy, monochrome designs. We are looking for new packaging designs and would like this new packaging to consist of a box with a window at the front to see and feel muslin wrap. Each box will hold one wrap (please see some examples of style of box we are after attached). Our logo (Ned and Rosie) should be on the front of the box. We are open to any colour options/illustrations on the box but would like it to stand out if placed on a shelf in a store. We would be interested in seeing a white box with monochrome designs across box.. Gold writing would also be great to see. There will be some additional info that will need to go on the back of the box.
Target Market(s)
women 20-40 year of age.
Industry/Entity Type
Baby
Requirements
Must have
- Logo
- Box design with window

```html
<!DOCTYPE html>
<html lang="en">
<head>
<meta charset="utf-8">
<title>Ned and Rosie – Baby Muslin Wrap Box Dieline</title>
<link rel="stylesheet" href="https://fonts.googleapis.com/css2?family=Marck+Script&family=Quicksand:wght@500&display=swap">
<style>
  :root {
    --backdrop: #0b1442;
    --board: #fbfaf1;
    --fold: #d9d9d4;
    --gold: #a8901f;
    --skin: #f2dfa6;
    --mint: #7fd3c0;
  }
  * { margin: 0; padding: 0; box-sizing: border-box; }
  html, body { width: 1200px; height: 970px; overflow: hidden; background: var(--backdrop); }
  .canvas { position: relative; width: 1200px; height: 970px; }
  .dieline { position: absolute; left: 0; top: 0; }
  .script { font-family: "Marck Script", cursive; font-weight: 400; color: var(--gold); white-space: nowrap; line-height: 1; }
  .brand-name { font-size: 15px; }
  .lid-title {
    position: absolute; left: 666px; top: 150px; transform: translate(-50%, -50%) rotate(180deg);
    display: flex; align-items: center; gap: 16px;
  }
  .lid-title .product-name { font-size: 28px; }
  .side-title {
    position: absolute; left: 496px; top: 335px; transform: translate(-50%, -50%) rotate(90deg);
    display: flex; flex-direction: column; align-items: center;
  }
  .side-title .product-name { font-size: 22px; }
  .side-title .fibre { font-family: "Quicksand", sans-serif; font-size: 9px; color: var(--gold); margin-top: 1px; }
  .side-brand { position: absolute; left: 464px; top: 220px; font-size: 13px; }
  .front-title {
    position: absolute; left: 666px; top: 524px; transform: translate(-50%, -50%);
    display: flex; align-items: center; gap: 16px;
  }
  .front-title .product-name { font-size: 28px; }
  .baby-art {
    position: absolute; left: 800px; top: 287px; width: 48px; height: 100px;
    background: linear-gradient(180deg, var(--board) 0%, var(--skin) 40%, var(--skin) 75%, var(--mint) 100%);
    border-radius: 14px;
  }
</style>
</head>
<body>
<main class="canvas">
  <svg class="dieline" width="1200" height="970" viewBox="0 0 1200 970">
    <polygon class="side-flap" points="456,203 432,185 349,185 323,217 323,465 349,473 368,496 433,496 456,473" fill="var(--board)"/>
    <polygon class="box-body" points="456,102 878,102 878,842 859,868 475,868 456,842" fill="var(--board)"/>
    <g class="fold-lines" stroke="var(--fold)" stroke-width="1">
      <line x1="456" y1="208" x2="878" y2="208"/>
      <line x1="456" y1="472" x2="878" y2="472"/>
      <line x1="456" y1="577" x2="878" y2="577"/>
      <line x1="456" y1="842" x2="878" y2="842"/>
      <line x1="349" y1="208" x2="349" y2="472"/>
      <line x1="456" y1="208" x2="456" y2="472"/>
    </g>
    <rect class="window" x="523" y="250" width="274" height="177" rx="14" fill="var(--backdrop)" stroke="var(--gold)" stroke-width="3"/>
    <g class="thumb-notches" fill="var(--backdrop)">
      <circle cx="878" cy="337" r="20"/>
      <circle cx="878" cy="711" r="20"/>
    </g>
  </svg>

  <div class="baby-art" role="img" aria-label="Illustration of a sleeping baby in a mint nappy peeking over the window"></div>

  <div class="lid-title">
    <span class="product-name script">Baby Muslin Wrap</span>
    <span class="brand-name script">Ned and Rosie</span>
  </div>

  <span class="side-brand script">Ned and Rosie</span>
  <div class="side-title">
    <span class="product-name script">Baby Muslin Wrap</span>
    <span class="fibre">100% Cotton</span>
  </div>

  <div class="front-title">
    <span class="brand-name script">Ned and Rosie</span>
    <span class="product-name script">Baby Muslin Wrap</span>
  </div>
</main>
</body>
</html>
```